Australian training business needs a flyer design it will use to promote its collaboration skills tr

We need a flyer that will promote our collaboration skills training short course. My business runs a series of short courses for corporate clients, such as presentation skills training and communications training. The flyer will most likely be sent to potential clients as a PDF, though it may also be printed, so I would like something that can be read on one page. It needs to excite them about training with us, this training is highly relevant for businesses building new teams and wanting people to work together well on projects. The training is also fun, so even though it's a corporate market they have a desire to be more creative and collaborative like the "creative industries", but they don't know how. Many of our clients work in the construction, industrial services and health industries - quite diverse. We want to make them think that this is the best 2.5 hours they could possibly spend.

Tandem Speakworks is the business name and I would like to see colours that reflect the logo, but I am not wedded to that. I suggest using the photo of Moira Calvetti (the trainer) small, if at all. If you use any stock photos I would prefer to see a mix of professional men and women working together, though I am not wedded to using stock imagery..industrial/technical feel with a creative flair might work.

Target Market(s)

Professional Business executives, ages 30 - 55

Industry/Entity Type

Training

Font styles to use
Sans Serif

Requirements
Must have
• Tandem Speakworks logo
• Course detail
• A Call to action:
• "Call or email Tandem Speakworks today to ask about our special course rate for existing clients"
Nice to have
• A look that appeals to the professions.
• Could include the price, I am undecided on this.
Should not have
• Bad American looking stock photos as we are an Australian company

```html
<!DOCTYPE html>
<html lang="en">
<head>
<meta charset="utf-8">
<title>Collaboration Skills Short Course – Tandem Speakworks</title>
<link rel="stylesheet" href="https://fonts.googleapis.com/css2?family=Oswald:wght@300;500;600;700&family=Jost:ital,wght@0,400;0,500;0,600;0,700;1,400;1,500&display=swap">
<style>
  :root {
    --lime: #b6c92f;
    --slate: #3d424b;
    --sky: #1aa1de;
    --white: #ffffff;
    --ink: #2f333a;
    --backdrop: #e8e5e0;
    --ring-blue: #2aa6d8;
    --ring-green: #b6c92f;
  }
  * { box-sizing: border-box; margin: 0; padding: 0; }
  html, body { width: 900px; height: 1200px; overflow: hidden; }
  body { background: var(--backdrop); font-family: "Jost", Arial, sans-serif; }

  .flyer { position: absolute; left: 68px; top: 47px; width: 749px; height: 1060px; background: var(--white); overflow: hidden; }
  .block { position: absolute; }

  .hero-panel { left: 0; top: 0; width: 373px; height: 525px; background: var(--lime); }
  .title-top { position: absolute; left: 33px; top: 50px; font: 700 45px/1 "Oswald", sans-serif; color: var(--white); letter-spacing: .5px; }
  .title-main { position: absolute; left: 33px; top: 92px; font: 700 118px/1 "Oswald", sans-serif; color: var(--slate); letter-spacing: 2px; }
  .title-sub { position: absolute; left: 34px; top: 200px; font: 300 33px/1 "Oswald", sans-serif; color: var(--white); }
  .challenge-box { position: absolute; left: 31px; top: 247px; width: 313px; height: 73px; background: var(--slate); border: 3px solid var(--white); color: var(--white); text-align: center; font: 600 27px/29px "Oswald", sans-serif; padding-top: 5px; letter-spacing: .3px; }
  .intro { position: absolute; left: 31px; top: 337px; width: 330px; font: italic 500 15.3px/21.6px "Jost", sans-serif; color: var(--ink); }

  .team-photo { left: 373px; top: 0; width: 376px; height: 320px; background: linear-gradient(135deg, #d8d4cf 0%, #eae7e3 45%, #b9a58f 70%, #5b6270 100%); }

  .outcomes-title { position: absolute; right: 35px; top: 346px; font: 600 20px/1 "Oswald", sans-serif; color: var(--sky); letter-spacing: .8px; }
  .outcomes { position: absolute; left: 392px; top: 386px; width: 340px; list-style: none; }
  .outcomes li { position: absolute; left: 0; padding-left: 39px; font: 600 15.2px/21.5px "Jost", sans-serif; color: var(--ink); }
  .outcomes .num { position: absolute; left: 0; top: -1px; width: 27px; height: 27px; border-radius: 50%; background: var(--sky); color: var(--white); font: 700 16px/27px "Jost", sans-serif; text-align: center; }

  .trainer-panel { left: 0; top: 525px; width: 373px; height: 333px; background: var(--slate); color: var(--white); }
  .trainer-heading { position: absolute; left: 35px; top: 17px; font: 600 24px/1 "Oswald", sans-serif; color: var(--lime); }
  .trainer-name { position: absolute; left: 35px; top: 56px; font: 700 13.5px/1 "Jost", sans-serif; }
  .trainer-roles { position: absolute; left: 35px; top: 73px; font: italic 400 12.5px/17.5px "Jost", sans-serif; }
  .trainer-photo { position: absolute; left: 223px; top: 13px; width: 121px; height: 107px; border: 4px solid var(--white); border-radius: 4px; background: linear-gradient(90deg, #d9b79a 0%, #c44a3f 100%); }
  .trainer-bio { position: absolute; left: 35px; width: 330px; font: 400 13px/18px "Jost", sans-serif; }
  .bio-one { top: 135px; }
  .bio-two { top: 218px; }

  .course-band { left: 373px; top: 738px; width: 376px; height: 120px; background: var(--slate); color: var(--white); text-align: center; font: 600 16px/23.5px "Jost", sans-serif; padding-top: 24px; letter-spacing: .3px; }

  .contact-panel { left: 0; top: 858px; width: 373px; height: 202px; background: var(--lime); }
  .contact-heading { position: absolute; left: 31px; top: 14px; font: 600 19px/1 "Oswald", sans-serif; color: var(--white); }
  .contact-name { position: absolute; left: 31px; top: 38px; font: 700 15px/1 "Jost", sans-serif; color: var(--ink); }
  .contact-role { position: absolute; left: 31px; top: 59px; font: italic 400 14.5px/1 "Jost", sans-serif; color: var(--ink); }
  .contact-list { position: absolute; left: 31px; top: 88px; list-style: none; }
  .contact-list li { display: flex; align-items: center; gap: 6px; height: 22px; font: 700 15px/1 "Jost", sans-serif; color: var(--ink); }
  .contact-list svg { width: 14px; height: 14px; flex: none; }

  .brand { left: 373px; top: 858px; width: 376px; height: 202px; display: flex; align-items: center; justify-content: center; gap: 16px; }
  .brand-ring { width: 74px; height: 74px; border: 2px solid var(--ring-blue); border-radius: 50%; flex: none; }
  .brand-name { font: 400 25px/1 "Jost", sans-serif; color: var(--slate); letter-spacing: 2px; }
</style>
</head>
<body>
<main class="flyer">

  <section class="block hero-panel">
    <h1>
      <span class="title-top">COLLABORATION</span>
      <span class="title-main">SKILLS</span>
      <span class="title-sub">SHORT COURSE (2.5 HOURS)</span>
    </h1>
    <p class="challenge-box">BRING A REAL-WORLD<br>CHALLENGE TO THE TABLE</p>
    <p class="intro">The Collaboration Skills course improves participants' ability to work together creatively as a team. It provides two processes that participants can use anytime, anywhere to work through a challenge. This workshop has a strong practical component and we recommend that the group brings a simple real-world challenge to the course to work on.</p>
  </section>

  <div class="block team-photo" role="img" aria-label="Photo of a smiling team of professional men and women seated together at a meeting table"></div>

  <section class="outcomes-section">
    <h2 class="outcomes-title">YOUR TEAM WILL…</h2>
    <ol class="outcomes">
      <li style="top:0"><span class="num">1</span>Discover the personal behaviour needed for successful collaboration to take place</li>
      <li style="top:80px"><span class="num">2</span>Learn practical skills from positive body language to listening with empathy</li>
      <li style="top:159px"><span class="num">3</span>Move away from the silo mentality and build trust</li>
      <li style="top:216px"><span class="num">4</span>Learn how to build a successful collaborative team from the ground up</li>
      <li style="top:275px"><span class="num">5</span>Learn a 6-step collaborative process for problem solving</li>
    </ol>
  </section>

  <section class="block trainer-panel">
    <h2 class="trainer-heading">Trainer</h2>
    <p class="trainer-name">Moira Calvetti,</p>
    <p class="trainer-roles">Principal, Tandem Speakworks<br>Managing Director,<br>Relay Productions</p>
    <div class="trainer-photo" role="img" aria-label="Portrait photo of trainer Moira Calvetti"></div>
    <p class="trainer-bio bio-one">I've been helping executives to look, act and sound like leaders for the past eight years, working with people in a variety of industries to ensure that their messages are crafted into persuasive presentations.</p>
    <p class="trainer-bio bio-two">Knowledge hoarding and the silo mentality of many in large organisations led me to develop courses to help people in business communicate and collaborate more effectively. I bring my small business creativity and communications experience to companies that are struggling to work together creatively.</p>
  </section>

  <p class="block course-band">The Collaboration Skills Short Course<br>is a 2.5 hour course for up to<br>8 people, at your premises.</p>

  <section class="block contact-panel">
    <h2 class="contact-heading">For more information</h2>
    <p class="contact-name">Moira Calvetti</p>
    <p class="contact-role">Principal</p>
    <ul class="contact-list">
      <li><svg viewBox="0 0 14 14" aria-hidden="true"><rect x="1" y="2" width="12" height="10" rx="1.5" fill="none" stroke="#fff" stroke-width="1.5"/><rect x="3.5" y="5" width="7" height="2" fill="#fff"/><rect x="3.5" y="8" width="2" height="2" fill="#fff"/><rect x="6" y="8" width="2" height="2" fill="#fff"/><rect x="8.5" y="8" width="2" height="2" fill="#fff"/></svg>(08) 6100 4820</li>
      <li><svg viewBox="0 0 14 14" aria-hidden="true"><rect x="3.5" y="0.8" width="7" height="12.4" rx="1.5" fill="none" stroke="#fff" stroke-width="1.5"/><circle cx="7" cy="10.8" r="0.9" fill="#fff"/></svg>0400 518 273</li>
      <li><svg viewBox="0 0 14 14" aria-hidden="true"><rect x="1" y="3" width="12" height="8" fill="#fff"/><path d="M1 3 L7 8 L13 3" fill="none" stroke="#b6c92f" stroke-width="1.2"/></svg>moira@tandemspeakworks.com</li>
      <li><svg viewBox="0 0 14 14" aria-hidden="true"><circle cx="7" cy="7" r="5.8" fill="none" stroke="#fff" stroke-width="1.3"/><ellipse cx="7" cy="7" rx="2.5" ry="5.8" fill="none" stroke="#fff" stroke-width="1.1"/><path d="M1.5 5h11M1.5 9h11" stroke="#fff" stroke-width="1.1"/></svg>www.tandemspeakworks.com</li>
    </ul>
  </section>

  <div class="block brand">
    <span class="brand-ring" aria-hidden="true"></span>
    <span class="brand-name">Tandem Speakworks</span>
  </div>

</main>
</body>
</html>
```